Financing service for small businesses

Need a flyer design promoting our Financing Service, look at the attachment to see the services we offer.
We are a CPA firm and provide a wide range of services including advisory services to small businesses that are trying to obtain bank financing.
The flyer should grab the attention of prospective businesses who need assistant with their financing needs.

Target Market(s)

Small Businesses

Industry/Entity Type

It Service

Font styles to use
Serif

Colors

Designer to choose colors to be used in the design.

Requirements
Must have
• Our Logo and address
• Why use our services
• Look Professional

```html
<!DOCTYPE html>
<html lang="en">
<head>
<meta charset="utf-8">
<title>Business Financing Services Flyer</title>
<link href="https://fonts.googleapis.com/css2?family=Cinzel:wght@400;600&family=Open+Sans:wght@400;700&display=swap" rel="stylesheet">
<style>
  :root {
    --bg: #e9eaec;
    --paper: #ffffff;
    --brand-blue: #1d5a9a;
    --heading-blue: #2166ad;
    --text: #3b3f45;
    --text-strong: #25292e;
    --sky-top: #ffffff;
    --sky-mid: #c9d6e0;
    --sky-low: #7d95a8;
    --sky-deep: #3d5b74;
  }
  * { box-sizing: border-box; margin: 0; padding: 0; }
  html, body { width: 1200px; height: 898px; overflow: hidden; background: var(--bg); }
  .flyer {
    position: absolute; left: 300px; top: 25px;
    width: 600px; height: 848px;
    background: var(--paper);
    box-shadow: 0 10px 30px rgba(0,0,0,0.12);
    overflow: hidden;
    font-family: "Open Sans", Arial, sans-serif;
    color: var(--text);
  }
  .brand {
    position: absolute; top: 48px; left: 0; width: 100%;
    display: flex; justify-content: center; align-items: center; gap: 16px;
  }
  .brand-square { width: 58px; height: 58px; background: var(--brand-blue); }
  .brand-text { display: flex; flex-direction: column; border-left: 2px solid var(--brand-blue); padding-left: 14px; }
  .brand-name { font-family: "Cinzel", Georgia, serif; font-size: 30px; font-weight: 600; color: var(--brand-blue); line-height: 1.1; }
  .brand-designation { font-family: "Cinzel", Georgia, serif; font-size: 14px; color: var(--brand-blue); letter-spacing: 1px; }
  .skyline {
    position: absolute; left: 0; right: 0; top: 470px; height: 318px;
    background: linear-gradient(to bottom, var(--sky-top) 0%, var(--sky-mid) 40%, var(--sky-low) 75%, var(--sky-deep) 100%);
  }
  .content { position: absolute; top: 150px; left: 50px; width: 505px; font-size: 10.5px; line-height: 1.38; }
  .section-title { font-size: 17px; font-weight: 400; color: var(--heading-blue); margin: 14px 0 2px; line-height: 1.2; }
  .content p { margin-bottom: 6px; }
  .lead { font-weight: 700; color: var(--text-strong); margin-top: 4px; }
  .bullets { list-style: none; margin-bottom: 6px; }
  .bullets li::before { content: "• "; }
  .footer-band {
    position: absolute; left: 0; right: 0; bottom: 0; height: 60px;
    background: var(--brand-blue); color: #fff;
    display: flex; justify-content: space-between; align-items: center;
    padding: 0 40px; font-size: 11px; font-weight: 700; letter-spacing: 0.5px;
  }
  .contact-line { display: flex; align-items: center; gap: 8px; }
  .phones { display: flex; flex-direction: column; gap: 3px; }
  .contact-icon { width: 12px; height: 12px; fill: #fff; }
</style>
</head>
<body>
<div class="flyer">
  <div class="brand">
    <div class="brand-square"></div>
    <div class="brand-text">
      <span class="brand-name">Northvale</span>
      <span class="brand-designation">Chartered Professional Accountants</span>
    </div>
  </div>

  <div class="skyline" role="img" aria-label="Aerial photograph of a city skyline fading into the sky"></div>

  <div class="content">
    <h1 class="section-title">Business Financing Services Calgary &amp; Vancouver</h1>
    <p>Financing is a key consideration for every business and is an integral part of allowing the business to properly plan for its future and realize its potential.</p>
    <p class="lead">Businesses require financing for many purposes, including:</p>
    <ul class="bullets">
      <li>Asset Purchases (expand the capacity of your existing business by investing in equipment)</li>
      <li>Working Capital (helping to manage the short term cash flow pain that comes with increased business, usually from having to carry more inventory or a larger receivable balance from customers)</li>
      <li>Growth Capital (investing in expanding the your company's product or service offering)</li>
      <li>Mergers &amp; Acquisitions (acquiring another company to increase the size or scale of your business)</li>
      <li>Corporate Restructuring and Refinancing</li>
    </ul>
    <p class="lead">When considering financing alternatives it is important to have an advisor that fully understands your company and its needs as well as the market in order to ensure the following:</p>
    <ul class="bullets">
      <li>Maximize the probability of obtaining the optimal financing</li>
      <li>The right amount of financing</li>
      <li>The most favorable terms</li>
      <li>The most reasonable cost of financing (there are often fees associated with the transaction which must be considered in addition to the interest rate on a debt instrument)</li>
      <li>The best source of financing (lender or investor).</li>
    </ul>
    <h2 class="section-title">Financing Types</h2>
    <p style="margin-bottom:0">The types of financing used to meet financing needs might include:</p>
    <ul class="bullets">
      <li>Conventional Term Loans (a loan that is paid back over a specific period of time, usually offered by one of the Big Banks)</li>
      <li>Operating Loans (normally used for working capital, the balance usually fluctuates with the business)</li>
      <li>Revolving Lines of Credit</li>
      <li>Project Financing (secured and used to fund a very specific activity of the business)</li>
      <li>Factoring (often used against accounts receivable in order to turn receivables to cash more quickly than simply waiting for the customer to pay)</li>
      <li>Subordinated Debt</li>
      <li>Venture Capital</li>
      <li>Angel Capital</li>
    </ul>
  </div>

  <div class="footer-band">
    <div class="contact-line">
      <svg class="contact-icon" viewBox="0 0 24 24" aria-hidden="true"><path d="M12 2a7 7 0 0 0-7 7c0 5 7 13 7 13s7-8 7-13a7 7 0 0 0-7-7zm0 9.5A2.5 2.5 0 1 1 12 6.5a2.5 2.5 0 0 1 0 5z"/></svg>
      <span>1480-3200 LARCHMONT ROAD SE<br>CALGARY, AB, T2P 3L9</span>
    </div>
    <div class="phones">
      <div class="contact-line">
        <svg class="contact-icon" viewBox="0 0 24 24" aria-hidden="true"><path d="M6.6 10.8a15 15 0 0 0 6.6 6.6l2.2-2.2c.3-.3.7-.4 1-.2 1.1.4 2.3.6 3.6.6.6 0 1 .4 1 1V20c0 .6-.4 1-1 1A17 17 0 0 1 3 4c0-.6.4-1 1-1h3.5c.6 0 1 .4 1 1 0 1.3.2 2.5.6 3.6.1.3 0 .7-.2 1z"/></svg>
        <span>(403) 555 0142</span>
      </div>
      <div class="contact-line">
        <svg class="contact-icon" viewBox="0 0 24 24" aria-hidden="true"><path d="M6 3h10v5H6zM4 9h16a2 2 0 0 1 2 2v7h-4v3H6v-3H2v-7a2 2 0 0 1 2-2zm4 7v3h8v-3z"/></svg>
        <span>(403) 555 0187</span>
      </div>
    </div>
  </div>
</div>
</body>
</html>
```